Overview of Elder Abuse Resources Brochure

We need a 2-page brochure that provides a list of resources for elders in tribal communities in the US and those who care for them. We want it to be simple and easy to read, and easy to see the difference between each resource. We would also like eye-catching images or graphics. Please keep the images on the front, and add any photos or graphics that depict Native American elders. We need both of our logos on the first page, in the far-right column. Please refer to the attached image for our brand colors and a font suggestion. Please keep the three columns on each page, but delete the blank pages in the document.

```html
<!DOCTYPE html>
<html lang="en">
<head>
<meta charset="utf-8">
<title>Elder Resources Brochure</title>
<link href="https://fonts.googleapis.com/css2?family=Oswald:wght@500;700&family=Roboto:wght@400;500;700&display=swap" rel="stylesheet">
<style>
:root{
  --rust:#b55a52;
  --teal:#4fa7b1;
  --ink:#222;
  --mist:#eaf4f6;
  --backdrop:#a9a9a9;
  --white:#fff;
}
*{box-sizing:border-box;margin:0;padding:0}
html,body{width:819px;height:1200px;overflow:hidden;background:var(--backdrop)}
body{position:relative;font-family:"Roboto",sans-serif;color:var(--ink)}
.page{position:absolute;left:78px;width:663px;height:512px;background:var(--white);overflow:hidden}
.page-front{top:74px}
.page-inside{top:615px}
.col{position:absolute;top:0;height:100%;width:221px}
.col-1{left:0}.col-2{left:221px}.col-3{left:442px}
.display{font-family:"Oswald",sans-serif;font-weight:700;text-transform:uppercase;line-height:1}
.rust{color:var(--rust)}.teal{color:var(--teal)}
.icon{display:inline-flex;align-items:center;justify-content:center;border-radius:50%;background:var(--rust);flex:none}
.icon svg{fill:var(--white)}
.photo{position:absolute}
.dove{position:absolute;width:34px;height:38px;border-radius:50%;background:radial-gradient(circle,rgba(181,90,82,.18),rgba(181,90,82,0) 70%)}

/* front: column 1 */
.respect-title{position:absolute;left:26px;top:23px;font-size:34px;line-height:35px}
.intro{position:absolute;left:27px;top:131px;width:175px;font-size:8.6px;line-height:15.5px;text-align:justify}
.help-heading{position:absolute;left:27px;top:286px;font-size:13px;font-weight:500}
.help-lead{position:absolute;left:27px;top:311px;width:175px;font-size:10.6px;line-height:17px}
.help-list{position:absolute;left:27px;top:352px;width:190px;list-style:none;font-size:8.8px;line-height:16.6px}
.help-list li{display:flex;gap:8px;align-items:flex-start;margin-bottom:0}
.help-list .icon{width:20px;height:20px;margin-top:-2px}

/* front: column 2 */
.col-contact{background:var(--teal)}
.contact-name{position:absolute;left:0;width:100%;top:232px;text-align:center;color:var(--white);font-family:"Oswald",sans-serif;font-weight:500;font-size:11px;line-height:13px;text-transform:uppercase}
.contact-title{position:absolute;left:31px;top:270px;color:var(--white);font-size:27px;letter-spacing:.5px}
.contact-list{position:absolute;left:32px;top:314px;list-style:none;color:var(--white);font-size:10.4px;line-height:17px}
.contact-list li{display:flex;gap:10px;align-items:center;margin-bottom:11px}
.contact-list .icon{width:24px;height:24px}

/* front: column 3 */
.org-name{position:absolute;left:0;width:100%;top:52px;text-align:center;font-family:"Oswald",sans-serif;font-weight:700;font-size:17px;line-height:20px;color:var(--teal);text-transform:uppercase}
.org-dot{display:block;width:30px;height:30px;margin:0 auto 8px;border-radius:50%;background:var(--teal)}
.services-title{position:absolute;left:0;width:100%;top:168px;text-align:center;font-size:21.5px;line-height:26px}
.caring-q{position:absolute;left:0;width:100%;top:254px;text-align:center;font-size:15px;line-height:18px;font-weight:700;color:var(--teal)}
.caring-text{position:absolute;left:0;width:100%;top:302px;text-align:center;font-size:11px;line-height:16.5px;z-index:2}
.photo-elder-shawl{left:0;top:325px;width:221px;height:187px;background:linear-gradient(180deg,rgba(255,255,255,1) 0%,rgba(255,255,255,.4) 22%,#8c3a48 55%,#5a2431 100%)}
.partner-badge{position:absolute;left:21px;top:386px;width:35px;height:35px;background:#1f2f3c}

/* inside: column 1 */
.stories-title{position:absolute;left:25px;top:155px;font-size:17px;line-height:20.5px}
.stories{position:absolute;left:27px;top:230px;width:175px;list-style:none;font-size:8.8px;line-height:15.5px}
.stories li{margin-bottom:0}
.stories li::before{content:"";display:inline-block;width:6px;height:6px;border-radius:50%;background:var(--teal);margin-right:8px;vertical-align:1px}
.hotline-band{position:absolute;left:0;bottom:0;width:224px;height:72px}
.hotline{position:absolute;left:17px;top:470px;display:flex;align-items:center;gap:8px;color:var(--white);font-weight:700;font-size:11.5px;line-height:18px}
.hotline .icon{width:23px;height:23px;background:var(--teal)}

/* inside: resources columns */
.col-resources{background:var(--mist);left:221px}
.res-title{position:absolute;top:27px;font-size:16.5px;letter-spacing:.2px}
.res-body{position:absolute;left:10px;top:57px;width:200px}
.col-3 .res-body{left:17px;top:134px}
.res-name{font-size:10.6px;font-weight:500;line-height:14px;margin-bottom:6px}
.col-3 .res-name{font-size:9.2px;line-height:12.5px;margin-bottom:4px}
.res-list{list-style:none;font-size:7.7px;line-height:14.5px;margin-bottom:10px}
.col-3 .res-list{line-height:12.3px;margin-bottom:10px}
.res-list li{display:flex;gap:6px;align-items:flex-start}
.res-list li.note{padding-left:17px;font-size:6.2px}
.res-list li.desc{padding-left:17px;line-height:11.5px}
.res-list .icon{width:10px;height:10px;margin-top:2px}
.res-list .icon svg{width:6px;height:6px}
.res-plain{font-size:7.7px;line-height:12px;margin-bottom:9px}
.kin-title{position:absolute;left:17px;top:349px;font-family:"Oswald",sans-serif;font-weight:500;font-size:9.3px}
.kin-body{top:364px}
.photo-caregiver{left:18px;top:57px;width:179px;height:70px;border-radius:6px;background:linear-gradient(120deg,#3b4a5c,#7d8f73 55%,#5a6b4c)}
.photo-grandkids{left:18px;top:272px;width:179px;height:70px;border-radius:6px;background:linear-gradient(120deg,#4b3226,#a0503e 50%,#6e4b3a)}
</style>
</head>
<body>

<svg width="0" height="0" style="position:absolute">
  <defs>
    <symbol id="i-phone" viewBox="0 0 24 24"><path d="M6.6 10.8a15.1 15.1 0 0 0 6.6 6.6l2.2-2.2c.3-.3.7-.4 1-.2 1.1.4 2.3.6 3.6.6.6 0 1 .4 1 1V20c0 .6-.4 1-1 1A17 17 0 0 1 3 4c0-.6.4-1 1-1h3.5c.6 0 1 .4 1 1 0 1.3.2 2.5.6 3.6.1.3 0 .7-.2 1z"/></symbol>
    <symbol id="i-pin" viewBox="0 0 24 24"><path d="M12 2a7 7 0 0 0-7 7c0 5.2 7 13 7 13s7-7.8 7-13a7 7 0 0 0-7-7zm0 9.5a2.5 2.5 0 1 1 0-5 2.5 2.5 0 0 1 0 5z"/></symbol>
    <symbol id="i-mail" viewBox="0 0 24 24"><path d="M3 5h18v14H3zm2 2v.5l7 4.5 7-4.5V7z"/></symbol>
    <symbol id="i-fax" viewBox="0 0 24 24"><path d="M4 8h4v12H4zm6 0h10v12H10zm2 3v2h2v-2zm4 0v2h2v-2zm-4 4v2h2v-2zm4 0v2h2v-2zM10 3h7v4h-7z"/></symbol>
    <symbol id="i-dot" viewBox="0 0 24 24"><circle cx="12" cy="12" r="7"/></symbol>
  </defs>
</svg>

<!-- Front page -->
<section class="page page-front">
  <div class="col col-1">
    <h1 class="display respect-title"><span class="rust">Respect</span><br><span class="teal">For</span><br><span class="rust">Elders</span></h1>
    <div class="dove" style="left:136px;top:75px" role="img" aria-label="Line drawing of a dove"></div>
    <p class="intro">Do you have concerns about an Elder, maybe you see that they are not taking care of themselves, or family only comes once a month when the Elder has money?<br>Is an Elder telling you that they are not treated with respect or that someone is bothering them?<br>These may be signs of Elder abuse, neglect or exploitation.</p>
    <h2 class="help-heading">For help contact:</h2>
    <p class="help-lead">Your Tribal Social Services or Elders Department:</p>
    <ul class="help-list">
      <li><span class="icon"><svg width="10" height="10"><use href="#i-phone"/></svg></span><span>The Elder Help Finder for information on Adult Protective Services 1-800-555-0116</span></li>
      <li><span class="icon"><svg width="10" height="10"><use href="#i-phone"/></svg></span><span>If a serious emergency, call 911.<br>For mental health support for yourself</span></li>
      <li><span class="icon"><svg width="10" height="10"><use href="#i-phone"/></svg></span><span>or an Elder, call or text 555-0188</span></li>
      <li><span class="icon"><svg width="10" height="10"><use href="#i-phone"/></svg></span><span>Domestic Violence Hotline<br>1.800.555.0172</span></li>
    </ul>
  </div>

  <div class="col col-2 col-contact">
    <svg class="photo" style="left:-221px;top:0" width="663" height="240" role="img" aria-label="Portrait of a smiling Native American elder woman in a circular frame">
      <circle cx="306" cy="17" r="136" fill="var(--rust)"/>
      <circle cx="306" cy="17" r="126" fill="var(--white)"/>
      <circle cx="306" cy="17" r="116" fill="#2a2420"/>
      <circle cx="306" cy="17" r="116" fill="url(#portraitTone)"/>
      <defs><radialGradient id="portraitTone" cx=".5" cy=".55" r=".5"><stop offset="0" stop-color="#8a6048"/><stop offset="1" stop-color="#1c1714"/></radialGradient></defs>
    </svg>
    <p class="contact-name">Circle of Elders<br>Care Network</p>
    <h2 class="display contact-title">Contact Us</h2>
    <ul class="contact-list">
      <li><span class="icon"><svg width="12" height="12"><use href="#i-pin"/></svg></span><span>123,Lorwm ipsum dolor<br>Sit Voluptinm Sit</span></li>
      <li><span class="icon"><svg width="12" height="12"><use href="#i-phone"/></svg></span><span>Domestic Violence Hotline<br>1.800.555.0172</span></li>
      <li><span class="icon"><svg width="12" height="12"><use href="#i-mail"/></svg></span><span>Email Us<br>info@companyname.com</span></li>
      <li><span class="icon"><svg width="12" height="12"><use href="#i-fax"/></svg></span><span>Fax<br>+1 999 999 99999</span></li>
    </ul>
  </div>

  <div class="col col-3">
    <p class="org-name"><span class="org-dot"></span>Circle of Elders<br>Care Network</p>
    <h2 class="display rust services-title">Services for Elders<br>&amp; People Who Care<br>For Them</h2>
    <p class="caring-q">Are you caring for an<br>Elder or a Grandchild?</p>
    <div class="photo photo-elder-shawl" role="img" aria-label="Native American elder woman wrapped in a colourful woven shawl and headscarf"></div>
    <p class="caring-text">Are you an Elder who needs<br>help staying at home?<br>These programs and information<br>can be a helpful resource.</p>
    <div class="partner-badge" role="img" aria-label="Partner badge"></div>
  </div>
</section>

<!-- Inside page -->
<section class="page page-inside">
  <div class="col col-1">
    <svg class="photo" style="left:0;top:0" width="224" height="150" role="img" aria-label="Portrait of a laughing Native American elder woman with braided hair">
      <defs><linearGradient id="laughTone" x1="0" y1="0" x2="1" y2="1"><stop offset="0" stop-color="#d8c3ad"/><stop offset=".6" stop-color="#8d5a6e"/><stop offset="1" stop-color="#6b3f7a"/></linearGradient></defs>
      <circle cx="92" cy="-6" r="144" fill="var(--rust)"/>
      <circle cx="92" cy="-6" r="136" fill="var(--white)"/>
      <circle cx="92" cy="-6" r="128" fill="url(#laughTone)"/>
    </svg>
    <div class="dove" style="left:160px;top:134px" role="img" aria-label="Line drawing of a dove"></div>
    <h2 class="display stories-title"><span class="rust">Do these stories</span><br><span class="teal">sound familiar</span><br><span class="rust">to you?</span></h2>
    <ul class="stories">
      <li>My mother gets lost driving home from the store.</li>
      <li>I need help getting groceries and with chores at home.</li>
      <li>My dad wants to sleep all the time; he doesn't go out with friends anymore. He stopped drumming.</li>
      <li>My sister is raising 3 grandchildren on her own.</li>
      <li>My son is disrespecting me. He only comes to visit when my retirement money arrives. He always asks for money.</li>
    </ul>
    <svg class="hotline-band" viewBox="0 0 224 72" preserveAspectRatio="none"><path d="M0 10 Q110 -8 205 20 Q224 30 224 72 L0 72 Z" fill="var(--rust)"/></svg>
    <div class="hotline"><span class="icon"><svg width="11" height="11"><use href="#i-phone"/></svg></span><span>Domestic Violence Hotline<br>1.800.555.0172</span></div>
  </div>

  <div class="col col-2 col-resources">
    <h2 class="display res-title" style="left:10px"><span class="rust">Resources</span> <span class="teal">for Elders</span></h2>
    <div class="dove" style="left:165px;top:57px" role="img" aria-label="Line drawing of a dove"></div>
    <div class="res-body">
      <h3 class="res-name">Elder Help Finder</h3>
      <ul class="res-list">
        <li><span class="icon"><svg><use href="#i-dot"/></svg></span>https://elderhelpfinder.example.org/home</li>
        <li><span class="icon"><svg><use href="#i-phone"/></svg></span>Call or Text: 1-800-555-0116</li>
        <li><span class="icon"><svg><use href="#i-mail"/></svg></span>Email: finder@elderhelp.example.org</li>
        <li class="note">For help finding support. Ask about services to Tribal Elders.</li>
      </ul>
      <h3 class="res-name">Memory Care Call Line</h3>
      <ul class="res-list">
        <li><span class="icon"><svg><use href="#i-dot"/></svg></span>(24 hours 7 days a week)</li>
        <li><span class="icon"><svg><use href="#i-phone"/></svg></span>Call 1-800-555-0139</li>
        <li class="desc">For support for people living with dementia, caregivers, families and the public. Connect with a live person who can provide information, local resources, crisis assistance and emotional support.</li>
      </ul>
      <h3 class="res-name">Crisis Support Lifeline</h3>
      <ul class="res-list">
        <li><span class="icon"><svg><use href="#i-phone"/></svg></span>For mental health support, call or text 555-0188.</li>
      </ul>
      <h3 class="res-name">State &amp; Tribal Hotlines | Tribal Elder Justice Project</h3>
      <ul class="res-list">
        <li class="desc" style="line-height:14.5px">To find local resources within your tribe or state that specialize in elder abuse, neglect or exploitation, visit:</li>
        <li><span class="icon"><svg><use href="#i-dot"/></svg></span>https://elderscircle.example.org/justice/state-tribal-hotlines/</li>
      </ul>
      <h3 class="res-name">Sacred Circle Native Helpline</h3>
      <ul class="res-list">
        <li><span class="icon"><svg><use href="#i-dot"/></svg></span>A 24/7 safe, confidential and anonymous domestic and sexual violence helpline for Native Americans and Alaska Natives.</li>
        <li><span class="icon"><svg><use href="#i-phone"/></svg></span>Call 1-844-555-0148</li>
        <li><span class="icon"><svg><use href="#i-phone"/></svg></span>(1-844-5NATIVE)</li>
        <li><span class="icon"><svg><use href="#i-dot"/></svg></span>https://sacredcirclehelpline.example.org/</li>
      </ul>
    </div>
  </div>

  <div class="col col-3">
    <h2 class="display res-title" style="left:15px"><span class="rust">Resources</span> <span class="teal">for Caregivers</span></h2>
    <div class="photo photo-caregiver" role="img" aria-label="Young caregiver sitting with a smiling elder woman in a wheelchair"></div>
    <div class="res-body">
      <h3 class="res-name">Elder Help Finder</h3>
      <ul class="res-list">
        <li><span class="icon"><svg><use href="#i-dot"/></svg></span>https://elderhelpfinder.example.org/home</li>
        <li><span class="icon"><svg><use href="#i-phone"/></svg></span>Call or Text: 1-800-555-0116</li>
        <li><span class="icon"><svg><use href="#i-mail"/></svg></span>Email: finder@elderhelp.example.org</li>
        <li class="note" style="font-size:6.6px">For help finding support. Ask about services to Tribal Elders.</li>
      </ul>
      <h3 class="res-name">Memory Friends | Circle of Elders Care Network</h3>
      <ul class="res-list">
        <li class="note" style="line-height:9.5px">An interactive educational program to better understand what dementia is and how it affects people.</li>
        <li><span class="icon"><svg><use href="#i-dot"/></svg></span>https://elderscircle.example.org/memory-friends/</li>
      </ul>
    </div>
    <div class="photo photo-grandkids" role="img" aria-label="Grandmother weaving beside two young granddaughters"></div>
    <p class="kin-title"><span class="rust">Grandparents Raising</span> <span class="teal">Grandchildren</span> <span class="rust">(Kinship Care)</span></p>
    <div class="res-body kin-body" style="top:368px">
      <h3 class="res-name">KinCircleHub.example.org</h3>
      <p class="res-plain">An interactive website that seeks to share all relevant publicly available information impacting grandfamilies</p>
      <h3 class="res-name">Memory Friends | Circle of Elders Care Network</h3>
      <ul class="res-list" style="width:160px">
        <li class="desc" style="line-height:9.5px">A list of resources for grandparents raising grandchildren.</li>
        <li><span class="icon"><svg><use href="#i-dot"/></svg></span>https://elderscircle.example.org/resource/grandparent-resources/</li>
      </ul>
    </div>
    <div class="dove" style="left:178px;top:462px" role="img" aria-label="Line drawing of a dove"></div>
  </div>
</section>

</body>
</html>
```